New Website for Belcourt Manor at www.belcourt.com.au

A new logo has been designed (through pixel forge) and we now want to align the look and feel of our website at www.belcourt.com.au to the new logo. The content and page names (e.g. Grounds) will remain largely unchanged for the new site, so please submit a new look "Home" page, using our new logo, current text and any photos you choose from the existing gallery at our website. I have also attached the current "Home" page photos.

Industry/Entity Type

Accommodation

Number of Pages Required

1 page

Requirements
Must have
• Logo to be presented on white background.

```html
<!DOCTYPE html>
<html lang="en">
<head>
<meta charset="utf-8">
<title>Belcourt Manor – Accommodation</title>
<link href="https://fonts.googleapis.com/css2?family=Montserrat:wght@300;400;500&display=swap" rel="stylesheet">
<style>
:root{
  --blue:#0b63b1;
  --blue-deep:#0a3f70;
  --yellow:#fcd94b;
  --gold:#bf9700;
  --ink:#1b1b1b;
  --rule:#cfcfcf;
  --white:#ffffff;
}
*{margin:0;padding:0;box-sizing:border-box}
html,body{width:1200px;height:1200px;overflow:hidden;background:var(--white)}
body{position:relative;font-family:'Montserrat',Arial,sans-serif;color:var(--ink)}
.band{position:absolute;left:88px;width:1024px;height:375px;overflow:hidden}
.band-mansion{top:0;background:var(--blue)}
.band-bedrooms{top:375px;background:var(--yellow)}
.photo{position:absolute;inset:0}
.photo-lounge{background:linear-gradient(135deg,#efe2c6 0%,#c98f62 45%,#8b5a3a 75%,#3a2a22 100%);clip-path:polygon(0 0,432px 0,598px 375px,0 375px)}
.edge-navy{position:absolute;inset:0;background:var(--blue-deep);clip-path:polygon(432px 0,452px 0,598px 375px,590px 375px)}
.photo-bedroom{background:linear-gradient(160deg,#f2f0ec 0%,#e1ddd6 40%,#8fa9a6 70%,#7d8a8f 100%);clip-path:polygon(598px 0,1024px 0,1024px 375px,440px 375px)}
.edge-gold{position:absolute;inset:0;background:var(--gold);clip-path:polygon(594px 0,598px 0,440px 375px,424px 375px)}
.band-title{position:absolute;font-weight:300;font-size:37px;letter-spacing:1.5px;line-height:1}
.band-mansion .band-title{left:498px;top:38px;color:var(--white)}
.band-bedrooms .band-title{left:42px;top:35px;color:var(--ink)}
.feature{position:absolute;font-size:13.5px;line-height:21.6px;color:var(--white);white-space:nowrap}
.feature::before,.room::before{content:"»";position:absolute;left:-16px;top:-2px;font-size:17px;font-weight:500}
.feature.cont::before{content:none}
.room{position:absolute;left:63px;font-size:13.5px;line-height:21.6px;white-space:nowrap}
.room::before{left:-17px}
.options{position:absolute;top:808px;left:0;width:1200px;text-align:center}
.options h2{font-weight:300;font-size:37px;letter-spacing:2px;line-height:52px}
.divider{width:503px;height:1px;background:var(--rule);margin:4px auto 0}
.options p{margin:14px auto 0;font-size:13px;line-height:21.6px;white-space:nowrap}
.apartment-photo{position:absolute;left:552px;top:948px;width:560px;height:252px;background:linear-gradient(90deg,#ffffff 0%,#ece6df 22%,#cdbfae 50%,#8a6448 80%,#7a4f33 100%)}
.apartment{position:absolute;left:132px;top:988px;width:440px}
.apartment h3{font-weight:300;font-size:28px;letter-spacing:0.8px;line-height:36px;padding-bottom:4px;border-bottom:1px solid var(--ink);width:346px;white-space:nowrap}
.apartment p{margin-top:22px;font-size:12.8px;line-height:21.6px;white-space:nowrap}
.apartment p+p{margin-top:21.6px}
</style>
</head>
<body>

<section class="band band-mansion">
  <div class="photo photo-lounge" role="img" aria-label="Photo of the grand lounge with leather sofas, fireplace and tiled floor"></div>
  <div class="edge-navy"></div>
  <h2 class="band-title">GRAND MANSION</h2>
  <div class="feature" style="left:498px;top:91px">Regal entrance and sweeping staircase</div>
  <div class="feature" style="left:514px;top:123px">Stately lounge or ballroom with 18 foot panelled ceiling and gas-driven</div>
  <div class="feature cont" style="left:540px;top:145px">fireplace – fondly referred to as “The Harrington Room”</div>
  <div class="feature" style="left:537px;top:177px">Elegant formal dining room</div>
  <div class="feature" style="left:550px;top:210px">Large open living area</div>
  <div class="feature" style="left:564px;top:239px">New Guinea Rosewood gourmet kitchen with walk-in pantry</div>
  <div class="feature cont" style="left:591px;top:261px">and Vellmar appliances</div>
  <div class="feature" style="left:589px;top:291px">Ducted reverse-cycle air-conditioning</div>
  <div class="feature" style="left:602px;top:320px">Wireless Internet</div>
</section>

<section class="band band-bedrooms">
  <div class="photo photo-bedroom" role="img" aria-label="Photo of a bright bedroom with queen bed, trundle bed and balcony doors"></div>
  <div class="edge-gold"></div>
  <h2 class="band-title">BEDROOMS</h2>
  <div class="room" style="top:84px">King (Master) Suite<br>Sleeps 4 | King bed | Double sofa bed</div>
  <div class="room" style="top:135px">Balcony Suite<br>Sleeps 4 | Queen bed | Single bed | Trundle bed</div>
  <div class="room" style="top:185px">Central Suite<br>Sleeps 4 | Queen bed | 2 x Single beds</div>
  <div class="room" style="top:235px">Queen Suite<br>Sleeps 4 | 2 x Queen beds</div>
  <div class="room" style="top:286px">Bunk Room<br>Sleeps 6 | 3 x Bunk beds</div>
</section>

<section class="options">
  <h2>OPTIONS TO SLEEP MORE!</h2>
  <div class="divider"></div>
  <p>The owner’s private apartment and guest room are now available to the public. If you want more space or need to sleep up to 26 people<br>– Belcourt Manor can accommodate you.</p>
</section>

<div class="apartment-photo" role="img" aria-label="Photo of the owner's apartment living room with leather lounge and kitchen"></div>
<section class="apartment">
  <h3>OWNER’S APARTMENT</h3>
  <p>The open plan apartment contains a living room, dining area and<br>kitchen – plus a large bedroom with king size bed, ensuite and<br>walk-in robe.</p>
  <p>For special guests, the apartment is a fabulous haven in the heart<br>of the estate!</p>
</section>

</body>
</html>
```